Business Card Design

We have a group of different function companies owned and operated by one person. We are located in the Dallas Fort Worth area in Texas. We develop properties to where we are owners and develop properties that are not ours as well. We build custom homes and commercial buildings. We also do residential and commercial remodeling. We also own commercial properties in which we lease office space. We are trying to merge all we do into one card and have done so already into one website. We initially had thought of having a logo made with HV in nice attractive lettering maybe as a watermark. We are open to the color scheme but no neons or pastels.

Project Deadline Extended
Reason: I am needing 2 different cards for two businesses.

Industry/Entity Type

Residential

Contact Information for Business Card

Harwell Ventures
4826 Mabry Ln. Suite 417
Fennbrook, Ardmont 54109
Land Development
Residential and Commercial Construction
Commercial Real Estate
Dale Wintermoot
www.harwellgrp.example
dale@harwellgrp.example
Cell: 555-555-0142
Office: 555-555-0187
Fax: 5555550163

```html
<!DOCTYPE html>
<html lang="en">
<head>
<meta charset="utf-8">
<title>Harwell Ventures — Business Card</title>
<link rel="stylesheet" href="https://fonts.googleapis.com/css2?family=Open+Sans:wght@400;600&family=Arimo:wght@700&display=swap">
<style>
  :root {
    --page-bg: #f2f2f2;
    --card-dark: #1f0f08;
    --card-mid: #3a1d10;
    --card-glow: #4a2614;
    --gold: #d9b24a;
    --gold-light: #f3d77a;
    --gold-deep: #a57d22;
    --ink: #1a0d05;
    --text-light: #ffffff;
  }
  * { box-sizing: border-box; margin: 0; padding: 0; }
  html, body { width: 1200px; height: 900px; overflow: hidden; }
  body {
    background: var(--page-bg);
    font-family: "Open Sans", sans-serif;
    position: relative;
  }
  .business-card {
    position: absolute;
    left: 100px; top: 164px;
    width: 1000px; height: 572px;
    border-radius: 44px;
    overflow: hidden;
    background:
      radial-gradient(ellipse 55% 60% at 52% 32%, var(--card-glow) 0%, var(--card-mid) 40%, var(--card-dark) 100%);
  }
  .brand {
    position: absolute;
    left: 70px; top: 96px;
    display: flex; align-items: center; gap: 22px;
  }
  .brand-mark {
    width: 30px; height: 30px;
    border-radius: 50%;
    background: var(--gold);
  }
  .brand-name {
    font-family: "Open Sans", sans-serif;
    font-weight: 600;
    font-size: 60px;
    letter-spacing: 2px;
    color: var(--gold);
    text-transform: uppercase;
  }
  .services-band {
    position: absolute;
    left: 0; top: 286px;
    width: 100%; height: 30px;
    background: linear-gradient(90deg, var(--gold-deep), var(--gold-light) 35%, var(--gold) 65%, var(--gold-light));
    display: flex; align-items: center; justify-content: center;
  }
  .services-band p {
    font-family: "Arimo", sans-serif;
    font-weight: 700;
    font-size: 17.5px;
    color: var(--ink);
    letter-spacing: 0.2px;
  }
  .person {
    position: absolute;
    left: 0; top: 336px;
    width: 355px;
    text-align: right;
  }
  .person-name {
    font-weight: 600;
    font-size: 30px;
    color: var(--gold);
    line-height: 1.2;
  }
  .person-title {
    font-size: 21px;
    color: var(--text-light);
    margin-top: 2px;
  }
  .divider {
    position: absolute;
    left: 375px; top: 330px;
    width: 1.5px; height: 214px;
    background: var(--text-light);
    opacity: 0.85;
  }
  .contact-list {
    position: absolute;
    left: 392px; top: 326px;
    list-style: none;
  }
  .contact-list li {
    display: flex; align-items: flex-start; gap: 10px;
    font-size: 24px;
    line-height: 31px;
    color: var(--text-light);
  }
  .contact-list svg {
    width: 24px; height: 24px;
    margin-top: 4px;
    flex: none;
    fill: var(--gold);
  }
</style>
</head>
<body>
  <section class="business-card">
    <div class="brand">
      <span class="brand-mark"></span>
      <span class="brand-name">Harwell Ventures</span>
    </div>

    <div class="services-band">
      <p>LAND DEVELOPMENT, RESIDENTIAL AND COMMERCIAL CONSTRUCTION, COMMERCIAL REAL ESTATE</p>
    </div>

    <div class="person">
      <p class="person-name">Dale Wintermoot</p>
      <p class="person-title">President</p>
    </div>

    <div class="divider"></div>

    <ul class="contact-list">
      <li>
        <svg viewBox="0 0 24 24" aria-hidden="true"><path d="M7 1h10a2 2 0 0 1 2 2v18a2 2 0 0 1-2 2H7a2 2 0 0 1-2-2V3a2 2 0 0 1 2-2zm0 3v12h10V4zm5 14a1.5 1.5 0 1 0 0 3 1.5 1.5 0 0 0 0-3z"/></svg>
        <span>555-555-0142</span>
      </li>
      <li>
        <svg viewBox="0 0 24 24" aria-hidden="true"><path d="M6.6 10.8a15.1 15.1 0 0 0 6.6 6.6l2.2-2.2a1 1 0 0 1 1-.25 11.4 11.4 0 0 0 3.6.57 1 1 0 0 1 1 1V20a1 1 0 0 1-1 1A17 17 0 0 1 3 4a1 1 0 0 1 1-1h3.5a1 1 0 0 1 1 1c0 1.250.2 2.450.57 3.570a1 1 0 0 1-.25 1z"/></svg>
        <span>555-555-0187</span>
      </li>
      <li>
        <svg viewBox="0 0 24 24" aria-hidden="true"><path d="M7 2h8l3 3v4H7zM4 10h16a2 2 0 0 1 2 2v7a2 2 0 0 1-2 2H4a2 2 0 0 1-2-2v-7a2 2 0 0 1 2-2zm2 3v2h6v-2zm11 0a1 1 0 1 0 0 2 1 1 0 0 0 0-2z"/></svg>
        <span>5555550163</span>
      </li>
      <li>
        <svg viewBox="0 0 24 24" aria-hidden="true"><path d="M2 6a2 2 0 0 1 2-2h16a2 2 0 0 1 2 2v12a2 2 0 0 1-2 2H4a2 2 0 0 1-2-2zm2 .5v.3l8 5.2 8-5.2v-.3zm0 2.7V18h16V9.2l-8 5.2z"/></svg>
        <span>dale@harwellgrp.example</span>
      </li>
      <li>
        <svg viewBox="0 0 24 24" aria-hidden="true"><path d="M12 2a10 10 0 1 0 0 20 10 10 0 0 0 0-20zm6.9 6h-2.9a15.7 15.7 0 0 0-1.4-3.6A8 8 0 0 1 18.9 8zM12 4c.8 1.2 1.5 2.5 1.9 4h-3.8c.4-1.5 1.1-2.8 1.9-4zM4.3 14a8 8 0 0 1 0-4h3.4a16.5 16.5 0 0 0 0 4zm.8 2h2.9c.3 1.3.8 2.5 1.4 3.6A8 8 0 0 1 5.1 16zM8 8H5.1a8 8 0 0 1 4.3-3.6C8.8 5.5 8.3 6.7 8 8zm4 12c-.8-1.2-1.5-2.5-1.9-4h3.8c-.4 1.5-1.1 2.8-1.9 4zm2.3-6H9.7a14.7 14.7 0 0 1 0-4h4.6a14.7 14.7 0 0 1 0 4zm.3 5.6c.6-1.1 1.1-2.3 1.4-3.6h2.9a8 8 0 0 1-4.3 3.6zm1.7-5.6a16.5 16.5 0 0 0 0-4h3.4a8 8 0 0 1 0 4z"/></svg>
        <span>www.harwellgrp.example</span>
      </li>
      <li>
        <svg viewBox="0 0 24 24" aria-hidden="true"><path d="M12 3 1 12h3v9h6v-6h4v6h6v-9h3z"/></svg>
        <span>4826 Mabry Ln. Suite 417<br>Fennbrook, Ardmont 54109</span>
      </li>
    </ul>
  </section>
</body>
</html>
```